Flyer for Daycare

A Flyer for family group daycare
Specfs:
- One side english / Another Side spanish(the text for both sides is below)
- The flyer is for printing in 5" x 7" or 5.5" x 8.5"
- The address and phone number is the most important
Logo(see the attachment)
NYC Licensed
Children from 6 Weeks to 12 years old
Accepting All the Programs( TPB, OMW) and Private
CPR & First Aid Certified
Full Time, Part Time and After School
----------------------------------------------------------------------------
Provide Homework Assistance
Potty Training
Outdoor Activities
Nutritional Meals & Snack
Baby Wipes
Text in Spanish
Licencia por el estado de NY
Niños de 6 semanas a 12 años
Aceptando Todos los Programas (TPB, OMW) y Privado
Certificación en CPR y Primeros Auxilios
Tiempo completo, tiempo parcial y después de la escuela
----------------------------------------------------------------------------------------------
Actividades al aire libre
Asistencia con la tarea
Entrenamiento para ir al baño
Desayunos, Comidas y refrigerios nutricionales
Toallitas para bebé
582 E 416th ST
APT 4C
Bronx, NY, 10587
ig: @lumokidcare
555-718-2043
Target Market(s)
LAtin and Black, Bronx NY Area
Industry/Entity Type
Daycare service
Look and feel

```html
<!DOCTYPE html>
<html lang="en">
<head>
<meta charset="utf-8">
<title>Lumo Kid Care – Flyer</title>
<link href="https://fonts.googleapis.com/css2?family=Arimo:wght@400;600;700&family=Work+Sans:wght@300&display=swap" rel="stylesheet">
<style>
  :root {
    --backdrop: #c6c5c6;
    --paper: #ffffff;
    --purple: #8b3c8f;
    --purple-deep: #6e2c74;
    --red: #e31e25;
    --green: #1f9340;
    --violet: #8e3b90;
    --orange: #f39220;
    --navy: #233b8a;
    --ink: #1a1a1a;
    --peach: #fdd9b5;
    --sky: #b3dff2;
    --rule: rgba(255,255,255,0.55);
  }
  * { margin: 0; padding: 0; box-sizing: border-box; }
  html, body { width: 919px; height: 1200px; overflow: hidden; }
  body { background: var(--backdrop); position: relative; font-family: "Arimo", Arial, sans-serif; }

  .flyer { position: absolute; left: 97px; top: 94px; width: 725px; height: 1012px; background: var(--paper); overflow: hidden; }
  .flyer > * { position: absolute; }
  .band { left: 0; top: 0; width: 725px; height: 1012px; }

  .silhouette { border-radius: 46% 46% 40% 40%; }
  .silhouette-girl { left: 62px; top: 163px; width: 180px; height: 227px; background: var(--peach); }
  .silhouette-boy { left: 510px; top: 185px; width: 193px; height: 241px; background: var(--sky); }

  .word { line-height: 1; white-space: nowrap; }
  .thin { font-family: "Work Sans", Arial, sans-serif; font-weight: 300; font-size: 27px; letter-spacing: 6px; color: var(--ink); }
  .bold { font-family: "Arimo", Arial, sans-serif; font-weight: 700; font-size: 52px; letter-spacing: -0.5px; }
  .c-red { color: var(--red); } .c-green { color: var(--green); } .c-violet { color: var(--violet); }
  .c-orange { color: var(--orange); } .c-navy { color: var(--navy); }

  .kid-art { border-radius: 40px; }
  .kid-left { left: 94px; top: 406px; width: 132px; height: 156px; background: linear-gradient(180deg, #9a3a1a 0%, #e31e25 60%, #f3b36a 100%); }
  .kid-right { left: 494px; top: 368px; width: 136px; height: 175px; background: linear-gradient(180deg, #151515 0%, #233b8a 55%, #1f9340 100%); }

  .brand-name { left: 0; width: 725px; top: 580px; text-align: center; font-weight: 700; font-size: 52px; line-height: 1; color: #ffffff; }
  .tagline { left: 0; width: 725px; top: 652px; text-align: center; font-weight: 700; font-size: 13px; letter-spacing: 1.5px; color: #ffffff; text-transform: uppercase; }

  .features { left: 0; top: 707px; width: 725px; list-style: none; }
  .features li { position: relative; height: 35.5px; text-align: center; color: #fff; font-weight: 600; font-size: 15px; letter-spacing: 2.3px; line-height: 30px; }
  .features li .rule { position: absolute; left: 50%; transform: translateX(-50%); bottom: 2px; height: 1px; background: var(--rule); }

  .contact { left: 144px; top: 906px; width: 437px; height: 67px; }
  .contact-shadow { position: absolute; left: 0; top: 0; width: 437px; height: 67px; border-radius: 34px; background: var(--purple-deep); }
  .contact-pill { position: absolute; left: 6px; top: 0; width: 425px; height: 67px; border-radius: 34px; background: var(--orange); color: #fff; text-align: center; font-weight: 700; }
  .address { display: block; font-size: 15px; letter-spacing: 1px; padding-top: 12px; line-height: 16px; }
  .reach { display: flex; justify-content: center; align-items: center; gap: 8px; font-size: 22px; letter-spacing: 1px; margin-top: 6px; line-height: 23px; }
  .phone-icon { width: 23px; height: 23px; flex: none; }
</style>
</head>
<body>
  <main class="flyer">
    <svg class="band" viewBox="0 0 725 1012" aria-hidden="true">
      <path fill="#8b3c8f" d="M0 486 C10 468 30 455 62 454 C100 452 125 470 150 478 L590 438 C610 426 630 428 642 442 C662 450 682 440 700 432 C712 427 720 424 725 423 L725 1012 L0 1012 Z"/>
    </svg>

    <div class="silhouette silhouette-girl" role="img" aria-label="Faint peach silhouette of a jumping girl"></div>
    <div class="silhouette silhouette-boy" role="img" aria-label="Faint light blue silhouette of a jumping boy"></div>

    <span class="word thin" style="left:175px;top:75px">provide</span>
    <span class="word bold c-red" style="left:102px;top:101px">HOMEWORK</span>
    <span class="word thin" style="left:428px;top:116px">assistance</span>
    <span class="word bold c-green" style="left:171px;top:137px">OUTDOOR</span>
    <span class="word thin" style="left:443px;top:152px">activities</span>
    <span class="word thin" style="left:120px;top:190px">potty</span>
    <span class="word bold c-violet" style="left:217px;top:173px">TRAINING</span>
    <span class="word thin" style="left:51px;top:226px">nutritional</span>
    <span class="word bold c-orange" style="left:251px;top:213px;font-size:51px">MEALS &amp; SNACK</span>
    <span class="word thin" style="left:230px;top:266px">baby</span>
    <span class="word bold c-navy" style="left:319px;top:251px">WIPES</span>

    <div class="kid-art kid-left" role="img" aria-label="Cartoon girl in a red shirt jumping with arms raised"></div>
    <div class="kid-art kid-right" role="img" aria-label="Cartoon boy in a blue shirt and green shorts jumping with arms raised"></div>

    <div class="brand-name">Lumo Kid Care</div>
    <div class="tagline">Your tranquility, our priority · Tu tranquilidad, nuestra prioridad</div>

    <ul class="features">
      <li>NYC LICENSED<span class="rule" style="width:147px"></span></li>
      <li>CHILDREN FROM 6 WEEKS TO 12 YEARS OLD<span class="rule" style="width:417px"></span></li>
      <li>ACCEPTING ALL THE PROGRAMS (TPB, OMW) AND PRIVATE<span class="rule" style="width:560px"></span></li>
      <li>CPR &amp; FIRST AID CERTIFIED<span class="rule" style="width:263px"></span></li>
      <li>FULL TIME, PART TIME AND AFTER SCHOOL</li>
    </ul>

    <div class="contact">
      <div class="contact-shadow"></div>
      <div class="contact-pill">
        <span class="address">582 E 416th ST, APT 4C, Bronx, NY, 10587</span>
        <span class="reach">
          <span class="handle">ig:@lumokidcare</span>
          <svg class="phone-icon" viewBox="0 0 24 24" aria-hidden="true"><circle cx="12" cy="12" r="11" fill="#fff" stroke="#8b3c8f" stroke-width="1.5"/><path fill="#8b3c8f" d="M8.6 6.5c.4-.3 1-.2 1.2.3l.9 2c.2.4.1.8-.2 1.1l-.8.7c.6 1.3 1.6 2.3 2.9 2.9l.7-.8c.3-.3.7-.4 1.1-.2l2 .9c.5.2.6.8.3 1.2l-.9 1.1c-.4.5-1.1.7-1.7.5-3-1-5.4-3.4-6.4-6.4-.2-.6 0-1.3.5-1.7z"/></svg>
          <span class="phone">555-718-2043</span>
        </span>
      </div>
    </div>
  </main>
</body>
</html>
```